Amberline Picture Works Web Design

COMPANY: AMBERLINE PICTURE WORKS
LOCATION: SHANGHAI, CHINA
AREA: FILM/TV DRAMA/COMMERCIALS/GAME POST PRODUCTION, SOUND DESIGN, MUSIC, and GAME.
WEB STYLE: SIMPLE, PROFESSIONAL, TRUSTWORTHY

LANGUAGE: ENGLISH, CHINESE. (Same layout, different language)
UPDATE: AFTER PROJECT FINISHED, WE NEED UPDATE BY OURSELVES.

MAIN SUBJECT: 6
1 HOMEPAGE
2 ABOUT US
3 TEAM
4 SERVICES
5 FACILITY
6 CONTACT

add one page of JOB OPPORTUNITIES.

DETAILS
1 HOMEPAGE
SLOGAN: Amberline Picture Works provides a well-designed working environment which amplifies your team’s ability to reach their creative goals.

Our services include:
 Feature Films
 Music & Scoring
 Commercials
 ADR & Foley
 Sound & Picture Editorial
 Sound Design
 Video Game

2 ABOUT US
Amberline Picture Works is located in the premiere South-Bund area of Shanghai. Occupying a 5000 square meter Technical Building, Amberline Picture Works was built by a filmmaker for filmmakers, and is one of the largest, most versatile full-service post-production facilities in China.

Amberline Picture Works is positioning to be at the forefront of the latest technology. Our goal is to provide a comprehensive solution for the post-production needs of our clients. We offer two fully-equipped dubbing stages (one of which will be certified VORTAN SPHERA ELITE), a large variety of both picture and sound editing rooms, impressive Foley and ADR stages, a world-class scoring stage, and complete audio and video transfer services.

We can handle your entire project from editing all the way to the end of the final sound mix; all under one extremely comfortable roof. We fully realize that the true art is in listening to the needs of our clients and making their greatest vision a reality. To this end our creative team's expertise, with a network of sound supervisors, editors and mixers, will deliver the magic you need. Producers and directors will also find our richly appointed guest accommodations to be a comfortable and soothing place to wind up the day. Every aspect of your project will be taken care of by a skilled and dedicated team, in the way that is best suited to you.

3 TEAM
(attachment 01)

4 SERVICES
Sound Mix
ADR
FOLEY
MUSIC
Sound Design
Sound Edit
Picture Edit
for all the Films, TV Drama, Commercials, Video Games, Online Media
(attachment 02, use photo)

5 FACILITY
(attachment 03)

6 CONTACT
(attachment04)
with map

Reason: Designers work are great, my bosses will spend 1-2 days select one of these web design, and spend 1-2 days to make some change, maybe use new photos.

```html
<!DOCTYPE html>
<html lang="en">
<head>
<meta charset="utf-8">
<title>Amberline Picture Works</title>
<link rel="stylesheet" href="https://fonts.googleapis.com/css2?family=Arimo:wght@400;700&family=Roboto+Condensed:wght@700&display=swap">
<style>
  :root {
    --black: #000000;
    --white: #ffffff;
    --amber: #f7c20e;
    --nav-active: #1f9a2e;
    --footer-grey: #5f5f5f;
    --icon-grey: #505050;
    --copy-grey: #8a8a8a;
    --arrow-bg: rgba(90, 90, 90, 0.75);
    --spectrum: linear-gradient(90deg, #8b2a8c 0%, #2d6fc0 25%, #1aa6a0 45%, #f2d21c 65%, #e2141e 85%, #b01a6e 100%);
  }
  * { margin: 0; padding: 0; box-sizing: border-box; }
  html, body { width: 1200px; height: 686px; overflow: hidden; background: var(--black); }
  body { position: relative; font-family: "Arimo", Arial, sans-serif; color: var(--white); }

  .site-header { position: absolute; left: 0; top: 0; width: 1200px; height: 88px; background: var(--black); }
  .brand { position: absolute; left: 90px; top: 26px; font: 700 27px/32px "Arimo", Arial, sans-serif; color: var(--amber); letter-spacing: 0.2px; }
  .main-nav { position: absolute; top: 0; left: 0; width: 1200px; height: 88px; list-style: none; }
  .main-nav li { position: absolute; top: 40px; font-size: 12.5px; line-height: 14px; }
  .main-nav li.is-active::before { content: ""; position: absolute; left: -5px; top: -40px; width: 43px; height: 6px; background: var(--nav-active); }

  .spectrum-line { position: absolute; left: 0; width: 1200px; height: 2px; background: var(--spectrum); }
  .spectrum-line.top { top: 88px; }
  .spectrum-line.bottom { top: 612px; }

  .hero { position: absolute; left: 0; top: 90px; width: 1200px; height: 522px; overflow: hidden; }
  .hero-photo { position: absolute; inset: 0;
    background:
      radial-gradient(ellipse at 20% 70%, rgba(90,190,160,0.35), transparent 45%),
      radial-gradient(ellipse at 90% 15%, rgba(40,80,220,0.35), transparent 30%),
      radial-gradient(ellipse at 75% 25%, rgba(200,190,40,0.25), transparent 35%),
      linear-gradient(160deg, #3a3634 0%, #2a2725 45%, #1c1a19 100%); }
  .hero-copy { position: absolute; left: 0; top: 154px; width: 1200px; text-align: center; font-family: "Roboto Condensed", "Arial Narrow", sans-serif; font-weight: 700; text-shadow: 0 1px 3px rgba(0,0,0,0.6); }
  .hero-title { margin-left: 25px; font-size: 47px; line-height: 58px; color: var(--amber); }
  .hero-tagline { margin-left: 25px; font-size: 30px; line-height: 39px; color: var(--white); }
  .slider-arrow { position: absolute; width: 36px; height: 36px; border-radius: 50%; background: var(--arrow-bg); }
  .slider-arrow.prev { left: 88px; top: 230px; }
  .slider-arrow.next { left: 1079px; top: 212px; }
  .slider-arrow svg { position: absolute; left: 0; top: 0; }

  .site-footer { position: absolute; left: 0; top: 614px; width: 1200px; height: 72px; background: var(--black); }
  .follow-label { position: absolute; left: 90px; top: 20px; font: 700 28px/32px "Roboto Condensed", "Arial Narrow", sans-serif; color: var(--footer-grey); }
  .social-list { position: absolute; left: 237px; top: 20px; list-style: none; display: flex; gap: 7px; }
  .social-list li { width: 32px; height: 32px; border-radius: 50%; background: var(--icon-grey); }
  .copyright { position: absolute; right: 92px; top: 30px; font-size: 13px; line-height: 15px; color: var(--copy-grey); }
</style>
</head>
<body>
  <header class="site-header">
    <div class="brand">AMBERLINE PICTURE WORKS</div>
    <ul class="main-nav">
      <li class="is-active" style="left:618px">HOME</li>
      <li style="left:682px">ABOUT US</li>
      <li style="left:773px">TEAM</li>
      <li style="left:831px">SERVICES</li>
      <li style="left:910px">FACILITY</li>
      <li style="left:985px">CONTACT</li>
      <li style="left:1062px">CAREER</li>
    </ul>
  </header>
  <div class="spectrum-line top"></div>

  <section class="hero">
    <div class="hero-photo" role="img" aria-label="Close-up of a mixing console with illuminated knobs and buttons in a sound studio"></div>
    <div class="hero-copy">
      <h1 class="hero-title">AMBERLINE PICTURE WORKS</h1>
      <p class="hero-tagline">PROVIDES A&nbsp; WELL-DESIGNED WORKING ENVIRONMENT</p>
      <p class="hero-tagline">WHICH AMPLIFIES YOUR TEAM’S ABILITY TO REACH THEIR CREATIVE GOALS.</p>
    </div>
    <div class="slider-arrow prev" aria-label="Previous slide">
      <svg width="36" height="36" viewBox="0 0 36 36"><polyline points="21,10 14,18 21,26" fill="none" stroke="#fff" stroke-width="1.6"/></svg>
    </div>
    <div class="slider-arrow next" aria-label="Next slide">
      <svg width="36" height="36" viewBox="0 0 36 36"><polyline points="15,10 22,18 15,26" fill="none" stroke="#fff" stroke-width="1.6"/></svg>
    </div>
  </section>
  <div class="spectrum-line bottom"></div>

  <footer class="site-footer">
    <div class="follow-label">FOLLOW US</div>
    <ul class="social-list" aria-label="Social links">
      <li></li><li></li><li></li><li></li><li></li>
    </ul>
    <p class="copyright">Copyright © 2014 Amberline Picture Works. All Rights Reserved.</p>
  </footer>
</body>
</html>
```